Water Filter Company Needs Bizz Cards!!

Need business cards for my company. We sell whole home water filters and salt free water softeners. No more buying bottled water. Our filtering units filter out all heavy metals, chlorine, and VOC's, last 15 years, and are maintenance free and supply your whole home with spring quality alkaline water. Our Salt free water conditioners, eliminate hard water and scale, without lowering the ph, or TDS's (total Dissolved solids)

I think this is the color code we are using on my site. My logo looks good behind it. #192841

Website will be www.Brovexa.com

Industry/Entity Type

Water Purification

Contact Information for Business Card

For now, just insert standard Dummy text. I need these text lines for the info to be editable so i can make them for multiple employees. I do have Photoshop and illustrator, unless there is a simpler program i can use solely for biz cards

Font styles to use
Sans Serif

Requirements
Must have
• Use my preexisting logo.

www.BroVexa.com

Spring Quality Alkaline Water at every tap.

List out services. Whole Home Water Filters, Salt Free Water Softeners, Clarimont KT7, UV Sterilizers
Nice to have
• I think this is the color code we are using on my site. My logo looks good behind it. #192841 or black. Please no white or light blue backgrounds.

Maybe a picture of my tank.

Slogan like Spring Quality Alkaline Water at every tap.
And just list the services Whole Home Water Filters, Salt Free Water Softeners, Clarimont KT7, UV Sterilizers

I think I would like to not have a contrasting textured logo like I see on some of them. I may use it for my personal cards, but new employees may not want the extra expense.
Should not have
• A different logo than the one provided.

White or baby blue backgrounds. Use the color code, or blacks.

```html
<!DOCTYPE html>
<html lang="en">
<head>
<meta charset="UTF-8">
<title>Brovexa Business Cards</title>
<link rel="stylesheet" href="https://fonts.googleapis.com/css2?family=Poppins:wght@400;500;600;700&display=swap">
<style>
  :root {
    --navy: #192841;
    --navy-deep: #16223a;
    --sky: #3bb8ec;
    --silver: #c9ccd1;
    --text-light: #d9dde4;
    --backdrop: #1f2024;
  }
  * { margin: 0; padding: 0; box-sizing: border-box; }
  html, body { width: 1200px; height: 800px; overflow: hidden; }
  body {
    background: var(--backdrop);
    font-family: "Poppins", sans-serif;
    display: flex;
    align-items: center;
    justify-content: center;
    gap: 40px;
  }
  .card {
    position: relative;
    width: 540px;
    height: 310px;
    border-radius: 18px;
    background: var(--navy);
    overflow: hidden;
    box-shadow: 0 18px 40px rgba(0,0,0,.45);
  }
  .card-shapes { position: absolute; inset: 0; width: 100%; height: 100%; }
  .brand {
    position: absolute;
    display: flex;
    align-items: center;
    gap: 12px;
    font-weight: 700;
    letter-spacing: -1px;
  }
  .brand-dot { border-radius: 50%; background: var(--sky); flex: none; }
  .front .brand { left: 0; right: 0; top: 78px; justify-content: center; font-size: 58px; color: var(--silver); }
  .front .brand-dot { width: 18px; height: 18px; }
  .services {
    position: absolute;
    left: 0; right: 0; top: 168px;
    text-align: center;
    color: var(--text-light);
    font-size: 12.5px;
    line-height: 1.7;
  }
  .services .sep { color: var(--sky); padding: 0 6px; }
  .website {
    position: absolute;
    right: 24px;
    bottom: 16px;
    font-size: 13px;
    font-weight: 500;
    color: var(--navy);
  }
  .contact .brand { left: 36px; top: 38px; font-size: 48px; color: var(--silver); }
  .contact .brand-dot { width: 26px; height: 26px; }
  .person { position: absolute; left: 40px; top: 142px; }
  .person-name { color: var(--sky); font-weight: 700; font-size: 19px; letter-spacing: .3px; }
  .person-role { color: var(--text-light); font-size: 13px; margin-top: -2px; }
  .divider { position: absolute; left: 40px; top: 200px; width: 440px; height: 1px; background: var(--sky); }
  .details { position: absolute; left: 40px; top: 214px; list-style: none; }
  .details li {
    display: flex; align-items: center; gap: 8px;
    color: var(--text-light); font-size: 12.5px; line-height: 1.75;
  }
  .details svg { width: 13px; height: 13px; flex: none; }
  .address {
    position: absolute;
    right: 26px; top: 206px;
    text-align: right;
    color: var(--text-light);
    font-size: 11.5px;
    line-height: 1.45;
  }
</style>
</head>
<body>

  <section class="card front" aria-label="Card front">
    <svg class="card-shapes" viewBox="0 0 540 310" aria-hidden="true">
      <path d="M0,310 L0,298 L320,286 L320,310 Z" fill="var(--silver)"/>
      <path d="M320,310 L320,284 Q320,262 342,262 L540,262 L540,310 Z" fill="var(--sky)"/>
    </svg>
    <div class="brand"><span class="brand-dot"></span><span>Brovexa</span></div>
    <p class="services">
      Whole Home Water Filters<span class="sep">|</span>Salt Free Water Softeners<br>
      Clarimont KT7<span class="sep">|</span>UV Sterilizers
    </p>
    <span class="website">www.brovexa.com</span>
  </section>

  <section class="card contact" aria-label="Card back">
    <svg class="card-shapes" viewBox="0 0 540 310" aria-hidden="true">
      <path d="M330,0 Q470,40 540,150 L540,0 Z" fill="#ffffff" opacity=".03"/>
      <path d="M380,-10 Q440,110 540,190" fill="none" stroke="#ffffff" stroke-opacity=".05" stroke-width="40"/>
      <path d="M0,310 L0,298 L320,286 L320,310 Z" fill="var(--silver)"/>
      <path d="M320,310 L320,284 Q320,262 342,262 L540,262 L540,310 Z" fill="var(--sky)"/>
    </svg>
    <div class="brand"><span class="brand-dot"></span><span>Brovexa</span></div>
    <div class="person">
      <p class="person-name">DANIEL REYES</p>
      <p class="person-role">Manager</p>
    </div>
    <div class="divider"></div>
    <ul class="details">
      <li>
        <svg viewBox="0 0 16 16" aria-hidden="true"><circle cx="8" cy="8" r="7.5" fill="var(--sky)"/><path d="M5.2 4.2l1.4-.3.8 1.9-.9.7a5 5 0 0 0 2.4 2.4l.7-.9 1.9.8-.3 1.4c-3.6.2-6.2-2.4-6-6z" fill="var(--navy)"/></svg>
        84 0900 555 214
      </li>
      <li>
        <svg viewBox="0 0 16 16" aria-hidden="true"><circle cx="8" cy="8" r="7.5" fill="var(--sky)"/><rect x="4" y="5.2" width="8" height="5.6" rx=".8" fill="var(--navy)"/><path d="M4.3 5.6L8 8.4l3.7-2.8" fill="none" stroke="var(--sky)" stroke-width=".9"/></svg>
        hello@brovexa.com
      </li>
    </ul>
    <p class="address">42 Tran Phu Street<br>Ba Dinh, Ha Noi</p>
    <span class="website">www.brovexa.com</span>
  </section>

</body>
</html>
```